Business Card with many future opportunities awaiting

I work with many companies that have I need designers to develop quick projects for logo's business cards, banners etc. I would like to try Sketch hive for this simple project in hopes to come back and use the same designer for future projects.

This is a financial company that has many projects with lending services.

I need a business card made to be sleek somewhat modern, we will also need a simple logo made using The initials of the company KLT and maybe have an arrow going through the initials pointing up.

We like the colors purple, blue green or any rich colors ..but do not want the card to be to flashy. This is a conservative business..other colors or ideas can be used. They also want the card vertical or we can try horizontal front with logo and a vertical back with information.
Updates

These designs are much to modern for this company. Please be more conservative. Thank you so much!

Can you guys show some vertical designs rounded corners and light background darker colors. Not so bright

Target Market(s)

Very Wealthy Clients this card is for the Loan and Merchant Services

Industry/Entity Type

Conservative

Logo Text

KLT Velwick lending Allies (maybe with an arrow going up)

Font styles to use
Serif
Script

Requirements
Must have
• KLT
Velwick Lending Allies

Gerald Thornby
C.O.O.

7 Larkmoor Ave Suite4
Boca Raton, FL 3332

555-204-6637 main
555-731-9082 cell
555-204-6638 fax

Ger@KLT.example
www.KLT.example

The final finals I will need to be able to make changes of names and numbers etc.
Nice to have
• I would like to have a spot for Notes on card if possible
Rounded corner edges

Client likes the royalty looking logo I have included maybe try and incorporate and change it up a bit. This logo was copied from somewhere else.

```html
<!DOCTYPE html>
<html lang="en">
<head>
<meta charset="utf-8">
<title>Velwick Lending Allies – Business Card</title>
<link rel="stylesheet" href="https://fonts.googleapis.com/css2?family=Cinzel:wght@400;600&family=Open+Sans:wght@400;600;700&display=swap">
<style>
  :root {
    --purple: #b23fb8;
    --purple-dark: #9a2fa0;
    --green: #9acd4c;
    --green-text: #a6cf6a;
    --ink: #2b2b2b;
    --grey: #6e6e6e;
    --card: #ffffff;
    --stage: #e9e6e1;
  }
  * { margin: 0; padding: 0; box-sizing: border-box; }
  html, body { width: 1200px; height: 1023px; overflow: hidden; }
  body {
    background: var(--stage);
    font-family: "Open Sans", Arial, sans-serif;
    position: relative;
  }
  .card {
    position: absolute;
    background: var(--card);
    border-radius: 10px;
    box-shadow: 0 6px 18px rgba(0,0,0,0.18);
    overflow: hidden;
  }

  /* Vertical front card */
  .card-front { left: 110px; top: 150px; width: 400px; height: 660px; }
  .band {
    position: absolute; left: 0; top: 0; bottom: 0; width: 92px;
    background: linear-gradient(180deg, var(--purple), var(--purple-dark));
  }
  .band-mark {
    position: absolute; left: 0; width: 92px; top: 250px;
    text-align: center; color: #fff;
    font-family: "Cinzel", Georgia, serif; font-weight: 600; font-size: 30px;
    letter-spacing: 2px;
  }
  .identity { position: absolute; right: 30px; top: 34px; text-align: right; }
  .person-name {
    font-family: "Cinzel", Georgia, serif; font-size: 25px; color: var(--green-text);
    letter-spacing: 1px;
  }
  .person-title { font-size: 19px; color: var(--grey); letter-spacing: 1px; margin-top: 2px; }
  .contacts { position: absolute; right: 30px; top: 140px; list-style: none; }
  .contacts li {
    display: flex; justify-content: flex-end; align-items: center; gap: 8px;
    font-size: 17px; color: var(--ink); line-height: 26px;
  }
  .icon { width: 17px; height: 17px; border-radius: 3px; background: var(--green); display: inline-flex; align-items: center; justify-content: center; }
  .icon-spacer { width: 17px; height: 17px; display: inline-block; }
  .company-block { position: absolute; right: 30px; bottom: 40px; text-align: right; }
  .company-name { font-weight: 700; font-size: 17px; color: var(--green-text); }
  .address { font-size: 17px; color: var(--ink); line-height: 26px; }

  /* Horizontal back card */
  .card-back { left: 560px; top: 430px; width: 580px; height: 340px; }
  .back-title {
    position: absolute; left: 50px; top: 70px;
    font-family: "Cinzel", Georgia, serif; font-size: 30px; color: var(--purple);
    letter-spacing: 1px;
  }
  .back-mark {
    position: absolute; left: 330px; top: 140px;
    font-family: "Cinzel", Georgia, serif; font-weight: 600; font-size: 44px; color: var(--purple);
    letter-spacing: 3px;
  }
  .website {
    position: absolute; left: 50px; bottom: 50px;
    font-size: 15px; color: var(--ink); letter-spacing: 1px;
  }
</style>
</head>
<body>
  <section class="card card-front" aria-label="Business card front">
    <div class="band"></div>
    <div class="band-mark">KLT</div>

    <div class="identity">
      <p class="person-name">Gerald Thornby</p>
      <p class="person-title">C.O.O.</p>
    </div>

    <ul class="contacts">
      <li>555-204-6637 <span class="icon-spacer"></span></li>
      <li>555-731-9082
        <span class="icon"><svg width="11" height="11" viewBox="0 0 24 24"><path fill="#fff" d="M6.6 10.8a15 15 0 0 0 6.6 6.6l2.2-2.2c.3-.3.7-.4 1-.2 1.1.4 2.3.6 3.6.6.6 0 1 .4 1 1V20c0 .6-.4 1-1 1A17 17 0 0 1 3 4c0-.6.4-1 1-1h3.5c.6 0 1 .4 1 1 0 1.3.2 2.5.6 3.6.1.3 0 .7-.2 1z"/></svg></span></li>
      <li>555-204-6638
        <span class="icon"><svg width="11" height="11" viewBox="0 0 24 24"><rect x="5" y="3" width="14" height="6" fill="#fff"/><rect x="3" y="10" width="18" height="9" rx="2" fill="#fff"/><rect x="7" y="15" width="10" height="6" fill="#9acd4c" stroke="#fff" stroke-width="2"/></svg></span></li>
      <li>Ger@KLT.example
        <span class="icon"><svg width="11" height="11" viewBox="0 0 24 24"><rect x="2" y="5" width="20" height="14" rx="2" fill="#fff"/><path d="M3 6l9 7 9-7" stroke="#9acd4c" stroke-width="2" fill="none"/></svg></span></li>
    </ul>

    <div class="company-block">
      <p class="company-name">Velwick Lending Allies</p>
      <p class="address">7 Larkmoor Ave Suite4</p>
      <p class="address">Dunmere Bay, ST 482</p>
    </div>
  </section>

  <section class="card card-back" aria-label="Business card back">
    <p class="back-title">Velwick Lending Allies</p>
    <p class="back-mark">KLT</p>
    <p class="website">www.KLT.example</p>
  </section>
</body>
</html>
```